Womens Personal Training studio needs new year flyers

I need a double sided A5 flyer to attract Women / Mothers to my fitness business, Radiant Core Studio, in the new year.

My business colour is teal, I am located in Oakvale QLD Aus

Exclusive studio training for women. At Radiant Core Studio we don't make New years resolutions, we Empower you to make the changes for life!

examples of pain Q's: Do you feel guilty about wanting to do something for yourself? Do you worry about what exercises are safe post baby? Are you struggling to regain control of your body and your life?

Would you like to love yourself and your body as much as you lvoe your baby?

I work with women to apporpriately and progressivley rebuild their bodies post preganany. As the Leading specialist in Pre and Post Natal Rehabilitation and Fitness in Durnford, Marnie knows what it takes to find the right balance. With a vision of Empowering this generation to inspire the next, Marnie teaches skills for LIFE so you can lead your family to a Healthier, Fitter and Stronger future! Using a fusion of Pilates, Strength Conditioning and Cardio Marnie customises a plan for each individual. Your free consultation is waiting call now and learn the first steps to making the change Valued at $147 Don’t Miss out!! Marnie 0438 270 614

Quote to go with image "Marnie doesn't just help you achieve your weight loss goals she works with you to make sure you are 'Radiant Core Studio'." Tessa Brook July 2013

Target Market(s)

Women / Mothers

Industry/Entity Type

Training

Requirements
Must have
• call to action
contact details
Marnie Clarke
0438 270 614
marnie@radiantcorestudio.net.au
www.radiantcorestudio.net.au

```html
<!DOCTYPE html>
<html lang="en">
<head>
<meta charset="utf-8">
<title>Radiant Core Studio – Oakvale Queensland flyer</title>
<link rel="stylesheet" href="https://fonts.googleapis.com/css2?family=Comfortaa:wght@500;700&family=Arimo:wght@400;700&family=Archivo+Black&display=swap">
<style>
:root{
  --teal:#2a9aa2;
  --teal-soft:#63b5b6;
  --teal-deep:#0f6f76;
  --ink:#17353a;
  --ink-dark:#0d2a2e;
  --grey-band:#8a8f90;
  --mist:#dff1f3;
  --white:#ffffff;
  --photo-tone-a:#2f7d93;
  --photo-tone-b:#5fa3b8;
}
*{box-sizing:border-box;margin:0;padding:0}
html,body{width:1200px;height:840px;overflow:hidden;background:#fff}
body{font-family:"Arimo",Arial,sans-serif;position:relative}
.page{position:absolute;top:0;height:840px;overflow:hidden}
.page--front{left:0;width:594px;background:var(--white)}
.page--back{left:600px;width:600px;background:linear-gradient(160deg,#f4fbfc 0%,var(--mist) 55%,#c7e7ea 100%)}
.page-divider{position:absolute;left:594px;top:0;width:6px;height:840px;background:var(--ink-dark)}
.abs{position:absolute}

/* front */
.owner-tag{left:40px;top:0;width:246px;height:56px;background:var(--ink);border-radius:0 0 6px 6px;text-align:center;padding-top:8px}
.owner-tag__name{color:var(--white);font:700 26px/1 "Arimo",sans-serif;letter-spacing:.5px}
.owner-tag__place{color:var(--teal-soft);font:700 11.5px/1 "Arimo",sans-serif;letter-spacing:2.4px;margin-top:4px}
.brand-name{font-family:"Comfortaa",sans-serif;font-weight:500;color:var(--teal)}
.front-brand{left:22px;top:60px;font-size:54px;line-height:60px}
.brand-dot{border-radius:50%;background:var(--teal)}
.front-dot{left:512px;top:16px;width:56px;height:56px}
.intro-box{left:22px;top:137px;width:554px;height:93px;background:var(--teal-soft);border-radius:4px;padding:12px 12px}
.intro-box h2{color:var(--white);font:700 22px/1.1 "Arimo",sans-serif;letter-spacing:.3px}
.intro-box p{color:var(--ink-dark);font:700 15.5px/1.3 "Arimo",sans-serif;margin-top:6px}
.pain-list{left:22px;top:258px;list-style:none;color:var(--teal-deep);font:700 16px/1.45 "Arimo",sans-serif}
.photo{background:linear-gradient(180deg,var(--photo-tone-a),var(--photo-tone-b) 70%,#4b4f55);border:6px solid var(--white);box-shadow:0 2px 8px rgba(0,0,0,.35)}
.front-photo{left:12px;top:345px;width:316px;height:455px;transform:rotate(-1.5deg)}
.miss-badge{display:flex;align-items:center;justify-content:center;text-align:center;border-radius:50%}
.front-badge{left:410px;top:340px;width:164px;height:164px;background:#111;color:var(--white);font:400 30px/1.05 "Archivo Black",sans-serif}
.miss-badge span{transform:rotate(12deg)}
.quote-box{background:var(--grey-band);color:var(--white)}
.front-quote{left:332px;top:530px;width:262px;height:142px;padding:12px 16px 0 22px;font:700 16.5px/1.25 "Arimo",sans-serif}
.quote-cite{display:block;text-align:right;font-size:10.5px;letter-spacing:1px;color:var(--ink-dark);margin-top:6px}
.front-wave{left:0;top:690px;width:594px;height:150px}
.front-url{left:0;top:784px;width:594px;text-align:center;color:var(--white);font:700 35px/56px "Arimo",sans-serif}

/* back */
.back-tab{left:0;top:16px;width:38px;height:64px;background:var(--teal-soft);border-radius:0 4px 4px 0}
.back-brand{left:46px;top:44px;font-size:30px;line-height:36px}
.back-dot{left:336px;top:20px;width:40px;height:40px}
.place-tag{left:376px;top:16px;width:214px;height:60px;background:var(--teal-soft);border:3px solid var(--ink-dark);border-radius:4px;text-align:center;padding-top:6px;font:700 20px/1.1 "Arimo",sans-serif;letter-spacing:1.5px}
.place-tag__top{color:var(--white)}
.place-tag__bottom{color:var(--ink-dark)}
.question-box{left:30px;top:118px;width:558px;height:162px;background:var(--teal);padding:14px 14px;color:var(--white)}
.question-box h2{font:700 18.5px/1.3 "Arimo",sans-serif}
.question-box p{font:400 14px/1.45 "Arimo",sans-serif;margin-top:14px;letter-spacing:.4px;text-align:justify}
.back-photo{left:40px;top:298px;width:146px;height:180px;transform:rotate(-2deg)}
.back-quote{left:186px;top:326px;width:414px;height:98px;padding:16px 20px 0 30px;font:400 13px/1.35 "Arimo",sans-serif;text-align:justify}
.back-quote .quote-cite{font-size:10px}
.story{left:12px;top:490px;width:576px;color:var(--ink-dark);font:400 15px/1.42 "Arimo",sans-serif;text-align:justify}
.call{left:22px;top:622px;width:560px;color:var(--ink-dark);font:700 14.5px/1.4 "Arimo",sans-serif}
.value-tag{left:0;top:672px;width:300px;height:42px;background:var(--teal);color:var(--white);font:700 25px/42px "Arimo",sans-serif;padding-left:30px;letter-spacing:.5px;border-radius:0 4px 4px 0}
.contact-band{left:0;top:730px;width:600px;height:110px;background:linear-gradient(180deg,#0f3a3f,var(--ink-dark))}
.contact{left:30px;top:758px;color:var(--white);font:400 17px/1.3 "Arimo",sans-serif}
.contact strong{font-size:17px;display:block;font-weight:700}
.back-badge{left:408px;top:660px;width:186px;height:186px;background:radial-gradient(circle,#fff 55%,#d9f0f2 80%,var(--teal-soft) 100%);border:5px solid var(--teal);color:#111;font:400 30px/1.05 "Archivo Black",sans-serif}
</style>
</head>
<body>

<section class="page page--front">
  <div class="abs owner-tag">
    <div class="owner-tag__name">MARNIE CLARKE</div>
    <div class="owner-tag__place">OAKVALE QUEENSLAND</div>
  </div>
  <div class="abs brand-name front-brand">Radiant Core Studio</div>
  <div class="abs brand-dot front-dot"></div>

  <div class="abs intro-box">
    <h2>EXCLUSIVE STUDIO TRAINING FOR WOMEN.</h2>
    <p>At Radiant Core Studio we don't make New years resolutions.<br>We Empower you to make the changes for life!</p>
  </div>

  <ul class="abs pain-list">
    <li>• Do you feel guilty about wanting to do something for yourself?</li>
    <li>• Do you worry about what exercises are safe post baby?</li>
    <li>• Are you struggling to regain control of your body and your life?</li>
  </ul>

  <div class="abs photo front-photo" role="img" aria-label="Before and after side-profile photos of a client during and after pregnancy"></div>

  <div class="abs miss-badge front-badge"><span>DON’T<br>MISS<br>OUT!!</span></div>

  <svg class="abs front-wave" viewBox="0 0 594 150" preserveAspectRatio="none" aria-hidden="true">
    <path d="M0 30 C180 10 360 60 594 20 L594 150 L0 150 Z" fill="#2a9aa2"/>
    <path d="M0 70 C200 40 380 100 594 60 L594 150 L0 150 Z" fill="#0f6f76"/>
    <rect x="0" y="94" width="594" height="56" fill="#0d2a2e"/>
  </svg>

  <blockquote class="abs quote-box front-quote">
    "Marnie doesn't just help you achieve your weight loss goals she works with you to make sure you are 'Radiant Core Studio'."
    <cite class="quote-cite">-Tessa Brook July 2013</cite>
  </blockquote>

  <div class="abs front-url">www.radiantcorestudio.net.au</div>
</section>

<div class="page-divider"></div>

<section class="page page--back" style="left:600px">
  <div class="abs back-tab"></div>
  <div class="abs brand-name back-brand">Radiant Core Studio</div>
  <div class="abs brand-dot back-dot"></div>
  <div class="abs place-tag">
    <div class="place-tag__top">OAKVALE</div>
    <div class="place-tag__bottom">QUEENSLAND</div>
  </div>

  <div class="abs question-box">
    <h2>Would you like to love yourself and your body as much as you love your baby?</h2>
    <p>I work with women to appropriately and progressively rebuild their bodies post pregnancy. As the Leading specialist in Pre and Post Natal Rehabilitation and Fitness in Durnford,</p>
  </div>

  <div class="abs photo back-photo" role="img" aria-label="Small before and after side-profile photos of a client"></div>

  <blockquote class="abs quote-box back-quote">
    "Marnie doesn't just help you achieve your weight loss goals she works with you to make sure you are 'Radiant Core Studio'."
    <cite class="quote-cite">-Tessa Brook July 2013</cite>
  </blockquote>

  <p class="abs story">“Marnie knows what it takes to find the right balance. With a vision of Empowering this generation to inspire the next, Marnie teaches skills for LIFE so you can lead your family to a Healthier, Fitter and Stronger future! Using a fusion of Pilates, Strength Conditioning and Cardio Marnie customises a plan for each individual.”</p>

  <p class="abs call">Your free consultation is waiting call now and learn the first steps to making the change.</p>

  <div class="abs value-tag">VALUED AT $147</div>

  <div class="abs contact-band"></div>
  <div class="abs contact">
    Marnie Clarke &nbsp;•&nbsp; 0438 270 614
    <strong>marnie@radiantcorestudio.net.au</strong>
    <strong>www.radiantcorestudio.net.au</strong>
  </div>

  <div class="abs miss-badge back-badge"><span>DON’T<br>MISS<br>OUT!!</span></div>
</section>

</body>
</html>
```